Copper and Slate Mist NZ new website!

We are a new online vaping retailer and are looking for an awesome sleek website. We are going to be selling a variety of vaping products and gear. Our logo has just been developed and we would like to keep the website in line with the black, tan a white theme. We would like to trying watermarking or imposing the rottie into the background of the website on the home page, with the page being black and you can see the tan and white colours only.

Coding

Coded - Design and coding required

Number of Pages Required

2 page

Font styles to use
Serif
Sans Serif
Decorative

Requirements
Must have
• A home page and a standard page for products
• Stay in line with the colours in the logo

```html
<!DOCTYPE html>
<html lang="en">
<head>
<meta charset="utf-8">
<title>Products – Copper and Slate Mist NZ</title>
<link href="https://fonts.googleapis.com/css2?family=Amaranth:wght@400;700&family=Lato:wght@400;700;900&display=swap" rel="stylesheet">
<style>
  :root{
    --tan:#b5600e;
    --tan-dark:#9a4f0a;
    --ink:#1b1b1b;
    --strike:#8a2a12;
    --side:#f6f6f6;
    --rule:#c98a4a;
    --night:#1e1216;
    --white:#fff;
    --holder:#e6e2de;
  }
  *{box-sizing:border-box;margin:0;padding:0}
  html,body{width:798px;height:1200px;overflow:hidden}
  body{position:relative;background:var(--white);font-family:"Lato",sans-serif;color:var(--ink)}

  /* header */
  .site-header{position:absolute;left:0;top:0;width:798px;height:86px;background:var(--white)}
  .brand{position:absolute;left:165px;top:30px;display:flex;align-items:center;gap:5px;
    font:700 8px/1.15 "Lato",sans-serif;color:var(--tan);width:90px}
  .brand-dot{width:24px;height:24px;border-radius:50%;background:var(--tan);flex:none}
  .nav{position:absolute;left:281px;top:40px;font-size:6.2px;color:#333}
  .nav a{position:absolute;top:0;color:inherit;text-decoration:none;white-space:nowrap}
  .nav .current{font-weight:900;color:#111;border-bottom:1.5px solid var(--tan);padding-bottom:3px}
  .nav .caret{color:var(--tan);font-size:5px;margin-left:1px}
  .icons{position:absolute;left:564px;top:37px;display:flex;align-items:center;gap:8px}
  .icons .bar{width:1px;height:9px;background:#333}
  .badge{position:absolute;left:37px;top:-3px;width:7px;height:7px;border-radius:50%;background:#111;color:#fff;font:700 5px/7px "Lato",sans-serif;text-align:center}

  /* page title band */
  .page-band{position:absolute;left:0;top:87px;width:798px;height:73px;
    background:linear-gradient(100deg,#b4600f,#c1711e 40%,#a9560b 70%,#b8661a)}
  .page-band h1{font:700 17px/73px "Amaranth",sans-serif;color:var(--white);text-align:center}

  /* sidebar */
  .sidebar{position:absolute;left:0;top:160px;width:261px;height:813px;background:var(--side)}
  .side-title{position:absolute;left:172px;font:700 10px "Amaranth",sans-serif;color:var(--tan)}
  .cat-list{position:absolute;left:172px;top:202px;list-style:none;font-size:5.6px;color:#333}
  .cat-list li{height:13.5px}
  .cat-list li::before{content:"- ";color:var(--tan)}
  .refine-card{position:absolute;left:172px;top:313px;width:80px;height:150px;background:var(--white)}
  .refine-card h3{font:700 9.5px/1.15 "Amaranth",sans-serif;text-align:center;margin-top:12px}
  .refine-card .pic{position:absolute;left:12px;top:42px;width:56px;height:104px;background:var(--holder)}
  .special{position:absolute;left:172px;width:90px;height:32px}
  .special .thumb{position:absolute;left:0;top:0;width:22px;height:24px;background:var(--holder)}
  .special .name{position:absolute;left:36px;top:0;font:700 5px "Lato",sans-serif}
  .special .price{position:absolute;left:36px;top:8px;font-size:5px}
  .special .add{position:absolute;left:36px;top:17px;font:700 4px "Lato",sans-serif}

  .price .now{color:var(--tan)}
  .price .was{color:var(--strike);text-decoration:line-through;margin-left:2px}

  /* content */
  .section-title{position:absolute;left:285px;top:179px;font:900 9px "Lato",sans-serif}
  .promo{position:absolute;left:285px;top:204px;width:347px;height:78px;display:flex}
  .promo-text{width:116px;background:#140b0e;color:var(--white);padding:17px 0 0 13px}
  .promo-text .kicker{font-size:4px}
  .promo-text .headline{font:700 6px "Amaranth",sans-serif;color:#d27d20;margin-top:1px}
  .promo-text .from{font-size:7.5px;margin-top:7px}
  .promo-text .amount{font:400 16px/1 "Amaranth",sans-serif;color:#e59a3a}
  .promo-text .amount sup{font-size:7px;color:var(--white)}
  .promo-photo{flex:1;background:var(--holder);position:relative}
  .promo-frame{position:absolute;left:4px;top:5px;right:5px;bottom:3px;border:2px solid #b07b3a}

  .toolbar{position:absolute;left:293px;top:295px;width:340px;height:14px;font-size:5px}
  .view-icons{position:absolute;left:0;top:1px;display:flex;gap:6px}
  .sort-label{position:absolute;left:189px;top:4px;font-weight:700}
  .select{position:absolute;top:0;height:13px;border:1px solid #444;background:var(--white);padding:3px 4px;font-size:5px}
  .select::after{content:"▾";position:absolute;right:3px;top:2px;font-size:6px}
  .show-label{position:absolute;left:278px;top:4px;font-weight:700}

  .product-row{position:absolute;left:285px;width:347px;height:111px;display:grid;grid-template-columns:114px 119px 114px}
  .product{position:relative;text-align:center}
  .product + .product{border-left:1px solid var(--rule)}
  .product .pic{position:absolute;left:50%;top:4px;transform:translateX(-50%);width:70px;height:66px;background:var(--holder)}
  .product .name{position:absolute;left:0;right:0;top:73px;font:700 5px "Lato",sans-serif}
  .product .price{position:absolute;left:0;right:0;top:80px;font-size:5px}
  .btn{display:inline-block;background:var(--tan);color:var(--white);font:700 4.2px/10px "Lato",sans-serif;
    padding:0 7px;border-radius:5px;box-shadow:0 1px 0 var(--tan-dark);white-space:nowrap}
  .product .btn{position:absolute;left:50%;top:94px;transform:translateX(-50%)}

  /* footer */
  .site-footer{position:absolute;left:0;top:973px;width:798px;height:227px;background:var(--night);color:var(--white)}
  .footer-ghost{position:absolute;left:60px;top:25px;width:140px;height:190px;border-radius:50% 50% 30% 30%;
    background:radial-gradient(ellipse at center,rgba(255,255,255,.07),rgba(255,255,255,0) 70%)}
  .footer-mark{position:absolute;left:358px;top:-42px;width:82px;height:82px;border-radius:50%;background:var(--tan);
    display:flex;align-items:center;justify-content:center;text-align:center;font:700 7.5px/1.25 "Lato",sans-serif;color:var(--white);padding:12px}
  .foot-col{position:absolute;top:59px;font-size:6.5px}
  .foot-col h4{font:900 7px "Lato",sans-serif;letter-spacing:1.5px;color:var(--tan);margin-bottom:8px}
  .foot-col ul{list-style:none}
  .foot-col li{height:13.6px}
  .foot-col li::before{content:"•";color:var(--tan);margin-right:5px}
  .info-line{display:flex;align-items:center;gap:4px;margin-bottom:19px}
  .foot-col .btn{font-size:5.5px;line-height:18px;padding:0 11px;border-radius:9px;margin-top:20px}
  .copyright{position:absolute;left:0;right:0;top:193px;text-align:center;font-size:5.5px}
</style>
</head>
<body>

<header class="site-header">
  <div class="brand"><span class="brand-dot"></span>Copper and Slate Mist NZ</div>
  <nav class="nav">
    <a style="left:0">HOME</a>
    <a style="left:37px">ABOUT</a>
    <a style="left:76px" class="current">PRODUCTS<span class="caret">⌄</span></a>
    <a style="left:127px">GALLERY</a>
    <a style="left:172px">BLOG</a>
    <a style="left:206px">CONTACT US</a>
  </nav>
  <div class="icons">
    <svg width="11" height="11" viewBox="0 0 12 12"><circle cx="6" cy="3.5" r="3" fill="#b5600e"/><path d="M0 12c0-4 3-5.5 6-5.5S12 8 12 12z" fill="#b5600e"/></svg>
    <span class="bar"></span>
    <svg width="12" height="11" viewBox="0 0 13 12"><path d="M0 1h2.5l2 7h6l1.8-5H4" fill="none" stroke="#b5600e" stroke-width="1.4"/><circle cx="5.5" cy="10.5" r="1.2" fill="#b5600e"/><circle cx="9.5" cy="10.5" r="1.2" fill="#b5600e"/></svg>
    <span class="badge">6</span>
  </div>
</header>

<section class="page-band"><h1>Products</h1></section>

<aside class="sidebar"></aside>
<h2 class="side-title" style="top:177px">Categories</h2>
<ul class="cat-list">
  <li>Petshop</li><li>Small Pets</li><li>Pet Products</li><li>Featured</li><li>Pet Foods</li>
</ul>
<h2 class="side-title" style="top:297px">Refine Search</h2>
<div class="refine-card">
  <h3>Laborum<br>Eveniet</h3>
  <div class="pic" role="img" aria-label="Product photo: grooming glove"></div>
</div>
<h2 class="side-title" style="top:486px">Specials</h2>
<div class="special" style="top:510px"><div class="thumb" role="img" aria-label="Product photo: bird seed bag"></div><div class="name">Lorem Ipsum</div><div class="price"><span class="now">$40.00</span><span class="was">$50.00</span></div><div class="add">Add to Cart</div></div>
<div class="special" style="top:548px"><div class="thumb" role="img" aria-label="Product photo: dog harness"></div><div class="name">Lorem Ipsum</div><div class="price"><span class="now">$40.00</span><span class="was">$50.00</span></div><div class="add">Add to Cart</div></div>
<div class="special" style="top:585px"><div class="thumb" role="img" aria-label="Product photo: dog food bag"></div><div class="name">Lorem Ipsum</div><div class="price"><span class="now">$40.00</span><span class="was">$50.00</span></div><div class="add">Add to Cart</div></div>
<div class="special" style="top:623px"><div class="thumb" role="img" aria-label="Product photo: dog leash"></div><div class="name">Lorem Ipsum</div><div class="price"><span class="now">$40.00</span><span class="was">$50.00</span></div><div class="add">Add to Cart</div></div>

<h2 class="section-title">Products</h2>
<div class="promo">
  <div class="promo-text">
    <div class="kicker">New Collection</div>
    <div class="headline">Pets Crooming &amp; Accesories</div>
    <div class="from">From</div>
    <div class="amount"><sup>$</sup>99.99</div>
  </div>
  <div class="promo-photo" role="img" aria-label="Promotional photo: dog resting on a beach"><span class="promo-frame"></span></div>
</div>

<div class="toolbar">
  <div class="view-icons">
    <svg width="9" height="9" viewBox="0 0 9 9" fill="none" stroke="#b5600e" stroke-width="1"><rect x=".5" y=".5" width="3" height="3"/><rect x="5.5" y=".5" width="3" height="3"/><rect x=".5" y="5.5" width="3" height="3"/><rect x="5.5" y="5.5" width="3" height="3"/></svg>
    <svg width="9" height="9" viewBox="0 0 9 9" fill="none" stroke="#333" stroke-width="1"><rect x=".5" y=".5" width="3" height="3"/><rect x=".5" y="5.5" width="3" height="3"/><path d="M5 1.5h4M5 3h3M5 6.5h4M5 8h3"/></svg>
  </div>
  <span class="sort-label">Sort By:</span>
  <div class="select" style="left:215px;width:60px">Default</div>
  <span class="show-label">Show:</span>
  <div class="select" style="left:299px;width:40px">9</div>
</div>

<div class="product-row" style="top:326px">
  <div class="product"><div class="pic" role="img" aria-label="Product photo: dog leash"></div><div class="name">Lorem Ipsum</div><div class="price"><span class="now">$40.00</span><span class="was">$50.00</span></div><span class="btn">Add to Cart</span></div>
  <div class="product"><div class="pic" role="img" aria-label="Product photo: dog harness"></div><div class="name">Lorem Ipsum</div><div class="price"><span class="now">$40.00</span><span class="was">$50.00</span></div><span class="btn">Add to Cart</span></div>
  <div class="product"><div class="pic" role="img" aria-label="Product photo: dog food bag"></div><div class="name">Lorem Ipsum</div><div class="price"><span class="now">$40.00</span><span class="was">$50.00</span></div><span class="btn">Add to Cart</span></div>
</div>
<div class="product-row" style="top:468px">
  <div class="product"><div class="pic" role="img" aria-label="Product photo: bird seed bag"></div><div class="name">Lorem Ipsum</div><div class="price"><span class="now">$40.00</span><span class="was">$50.00</span></div><span class="btn">Add to Cart</span></div>
  <div class="product"><div class="pic" role="img" aria-label="Product photo: dog leash"></div><div class="name">Lorem Ipsum</div><div class="price"><span class="now">$40.00</span><span class="was">$50.00</span></div><span class="btn">Add to Cart</span></div>
  <div class="product"><div class="pic" role="img" aria-label="Product photo: dog leash"></div><div class="name">Lorem Ipsum</div><div class="price"><span class="now">$40.00</span><span class="was">$50.00</span></div><span class="btn">Add to Cart</span></div>
</div>
<div class="product-row" style="top:610px">
  <div class="product"><div class="pic" role="img" aria-label="Product photo: dog leash"></div><div class="name">Lorem Ipsum</div><div class="price"><span class="now">$40.00</span><span class="was">$50.00</span></div><span class="btn">Add to Cart</span></div>
  <div class="product"><div class="pic" role="img" aria-label="Product photo: dog harness"></div><div class="name">Lorem Ipsum</div><div class="price"><span class="now">$40.00</span><span class="was">$50.00</span></div><span class="btn">Add to Cart</span></div>
  <div class="product"><div class="pic" role="img" aria-label="Product photo: dog food bag"></div><div class="name">Lorem Ipsum</div><div class="price"><span class="now">$40.00</span><span class="was">$50.00</span></div><span class="btn">Add to Cart</span></div>
</div>
<div class="product-row" style="top:751px">
  <div class="product"><div class="pic" role="img" aria-label="Product photo: bird seed bag"></div><div class="name">Lorem Ipsum</div><div class="price"><span class="now">$40.00</span><span class="was">$50.00</span></div><span class="btn">Add to Cart</span></div>
  <div class="product"><div class="pic" role="img" aria-label="Product photo: dog leash"></div><div class="name">Lorem Ipsum</div><div class="price"><span class="now">$40.00</span><span class="was">$50.00</span></div><span class="btn">Add to Cart</span></div>
  <div class="product"><div class="pic" role="img" aria-label="Product photo: dog leash"></div><div class="name">Lorem Ipsum</div><div class="price"><span class="now">$40.00</span><span class="was">$50.00</span></div><span class="btn">Add to Cart</span></div>
</div>

<footer class="site-footer">
  <div class="footer-ghost" role="img" aria-label="Faint background photo of a dog"></div>
  <div class="footer-mark">Copper and Slate Mist NZ</div>

  <div class="foot-col" style="left:226px">
    <h4>ADDRESS/MAP:</h4>
    <div class="info-line"><svg width="7" height="9" viewBox="0 0 7 9"><path d="M3.5 9S0 5.2 0 3.5a3.5 3.5 0 017 0C7 5.2 3.5 9 3.5 9z" fill="#b5600e"/><circle cx="3.5" cy="3.5" r="1.3" fill="#1e1216"/></svg>ABC Street City</div>
    <h4>OFFICE HOURS:</h4>
    <div class="info-line"><svg width="8" height="8" viewBox="0 0 8 8" fill="none" stroke="#b5600e"><circle cx="4" cy="4" r="3.4"/><path d="M4 2v2h1.6"/></svg>Monday To Friday&nbsp;<b>8am-5pm</b></div>
    <h4>PHONE:</h4>
    <div class="info-line" style="font-size:8.5px"><svg width="8" height="8" viewBox="0 0 8 8"><path d="M1.5 0l1.5 2-1 1a5 5 0 003 3l1-1 2 1.5L7 8C3 8 0 5 0 1z" fill="#b5600e"/></svg>(000) 000-0000</div>
  </div>

  <div class="foot-col" style="left:376px">
    <h4>PRACTICE AREAS</h4>
    <ul><li>Home</li><li>About</li><li>Products</li><li>Gallery</li><li>Blog</li><li>Contact Us</li></ul>
  </div>

  <div class="foot-col" style="left:519px">
    <h4>PRODUCTS</h4>
    <ul><li>Cagespets</li><li>Portpet</li><li>Foods</li></ul>
    <span class="btn">Make an Appointment</span>
  </div>

  <p class="copyright">Copyright 2019 Copper and Slate Mist NZ. All Right Reserved.</p>
</footer>

</body>
</html>
```